A5 Flyer for mobile App development

We need a double sided flyer design that will need to be printed on A5 sized paper.
The design will be based on a phone/tablet look and feel.

The idea behind the pamphlet is that we show clients that they can have a mobile app white labelled to their company/brand.

The front of the pamphlet will need to look like a front of a phone with a generic mobile app running within the phone.
The phone must not resemble a real phone, however, it should resemble a cartoon look phone - similar to the attached image called "phone.jpg". The mobile app running within the phone needs to have a "drawing/wireframe" look - similar to the "mock.jpg" image attached. The logo part should look like a "placeholder" image - similar to the image named "mocklogo" (look at the far left) attached.

The back of the pamphlet must also be similar, so that when you turn over the pamphlet, it should look like you're turning over a real phone, and you're now the seeing the back of the phone.
The back of the phone should be styled similar to the front. The text and items on the back of the phone are also in the image named "20170503_212415.jpg".

The phone on the pamphlet should not have an outline, meaning that the pamphlet will have rounded corners, giving the phone a shape.

Please send us a message if you're unsure about anything.

Target Market(s)

Businesses that have salons, spa's, beauty clinics, etc.

Industry/Entity Type

Health And Wellness

Font styles to use
Sans Serif
Script

Colors
e34297

Requirements
Must have
• The pamphlet will have rounded corners, giving the phone its look. See attached the image named "pingloom.."
Should not have
• the phone on the pamphlet should not have an outline, meaning that the pamphlet will have rounded corners, giving the phone a shape. Please have a look at the pingloom image attached that demonstrates the cut out lines.

```html
<!DOCTYPE html>
<html lang="en">
<head>
<meta charset="utf-8">
<title>App Flyer – Front and Back</title>
<link rel="stylesheet" href="https://fonts.googleapis.com/css2?family=Quicksand:wght@300;400;700&family=Ubuntu:wght@700&display=swap">
<style>
  :root {
    --page: #ffffff;
    --shell-front: #3f4650;
    --shell-back: #1c2027;
    --back-panel: #1f242c;
    --ring: #ffffff;
    --magenta: #e0389a;
    --sale-red: #f01414;
    --button-light: #93d83c;
    --button-dark: #5bb52a;
    --button-knob: #3f8a1f;
    --screen-light: #9fe6f7;
    --screen-mid: #5cc9ea;
    --screen-deep: #2aa6d6;
    --ink: #333a42;
    --metal: #d8dbdf;
  }
  html, body {
    margin: 0;
    padding: 0;
    width: 1200px;
    height: 1200px;
    overflow: hidden;
    background: var(--page);
  }
  .flyer { display: block; width: 1200px; height: 1200px; }
  .logo-placeholder-text { font-family: "Ubuntu", sans-serif; font-weight: 700; font-size: 40px; fill: var(--ink); }
  .headline { font-family: "Quicksand", sans-serif; font-weight: 700; font-size: 54px; fill: var(--magenta); }
  .cta-label { font-family: "Quicksand", sans-serif; font-weight: 700; font-size: 36px; fill: #ffffff; }
  .brand-name { font-family: "Quicksand", sans-serif; font-weight: 700; font-size: 48px; fill: #ffffff; letter-spacing: 10px; }
  .price { font-family: "Quicksand", sans-serif; font-weight: 700; font-size: 40px; fill: #ffffff; }
  .price-sale { font-family: "Quicksand", sans-serif; font-weight: 700; font-size: 42px; fill: var(--sale-red); }
  .pitch { font-family: "Quicksand", sans-serif; font-weight: 300; font-size: 40px; fill: #ffffff; }
  .platform { font-family: "Quicksand", sans-serif; font-weight: 700; font-size: 40px; fill: var(--magenta); }
  .contact { font-family: "Quicksand", sans-serif; font-weight: 400; font-size: 22px; fill: #ffffff; }
</style>
</head>
<body>
<svg class="flyer" viewBox="0 0 1400 1400" xmlns="http://www.w3.org/2000/svg">
  <defs>
    <linearGradient id="screenGlow" x1="0" y1="0" x2="1" y2="1">
      <stop offset="0" stop-color="var(--screen-light)"/>
      <stop offset="0.5" stop-color="var(--screen-mid)"/>
      <stop offset="1" stop-color="var(--screen-deep)"/>
    </linearGradient>
    <linearGradient id="ctaFill" x1="0" y1="0" x2="0" y2="1">
      <stop offset="0" stop-color="var(--button-light)"/>
      <stop offset="1" stop-color="var(--button-dark)"/>
    </linearGradient>
  </defs>

  <!-- Front of phone -->
  <g class="phone-front">
    <rect class="shell" x="40" y="230" width="648" height="940" rx="130" fill="var(--shell-front)"/>
    <rect class="ring" x="62" y="252" width="604" height="896" rx="110" fill="var(--ring)"/>
    <rect class="body" x="80" y="270" width="568" height="860" rx="94" fill="var(--shell-front)"/>

    <circle class="front-camera" cx="252" cy="318" r="8" fill="#1a2a44" stroke="#ffffff" stroke-width="2"/>
    <rect class="speaker" x="273" y="307" width="182" height="22" rx="11" fill="var(--metal)" stroke="#ffffff" stroke-width="2"/>

    <rect class="screen-gap" x="80" y="360" width="568" height="678" fill="var(--ring)"/>
    <rect class="screen" x="80" y="377" width="568" height="645" fill="url(#screenGlow)" role="img" aria-label="Light blue abstract network background of connected lines and dots"/>

    <circle class="logo-placeholder" cx="363" cy="540" r="90" fill="#ffffff"/>
    <circle cx="363" cy="540" r="83" fill="none" stroke="#1f1f1f" stroke-width="3"/>
    <text class="logo-placeholder-text" x="365" y="536" text-anchor="middle">YOUR</text>
    <text class="logo-placeholder-text" x="365" y="585" text-anchor="middle">LOGO</text>

    <text class="headline" x="363" y="733" text-anchor="middle">Believe in</text>
    <text class="headline" x="363" y="802" text-anchor="middle">something better</text>

    <g class="cta-button">
      <rect x="200" y="895" width="315" height="68" rx="34" fill="url(#ctaFill)"/>
      <text class="cta-label" x="226" y="943">BOOK NOW</text>
      <circle cx="476" cy="929" r="21" fill="var(--button-knob)"/>
      <circle cx="476" cy="929" r="10" fill="none" stroke="#ffffff" stroke-width="3"/>
    </g>

    <rect class="home-button" x="330" y="1055" width="68" height="57" rx="9" fill="#ffffff" stroke="#a9adb2" stroke-width="3"/>
  </g>

  <!-- Back of phone -->
  <g class="phone-back">
    <rect class="shell" x="713" y="230" width="648" height="940" rx="130" fill="var(--shell-back)"/>
    <rect class="ring" x="735" y="252" width="604" height="896" rx="110" fill="var(--ring)"/>
    <rect class="body" x="753" y="270" width="568" height="860" rx="94" fill="var(--back-panel)" role="img" aria-label="Black leather texture back panel"/>

    <g class="rear-camera">
      <circle cx="1037" cy="357" r="46" fill="#9aa0a6"/>
      <circle cx="1037" cy="357" r="40" fill="#111418"/>
      <circle cx="1037" cy="357" r="19" fill="#1e48a8"/>
      <circle cx="1120" cy="358" r="16" fill="#9aa0a6"/>
      <circle cx="1120" cy="358" r="8" fill="#dfe2e5"/>
    </g>

    <text class="brand-name" x="1042" y="514" text-anchor="middle">LUMA</text>

    <text class="price" x="884" y="617">From R <tspan>699</tspan> PM</text>
    <line class="price-strike" x1="1034" y1="612" x2="1116" y2="588" stroke="var(--sale-red)" stroke-width="3"/>
    <text class="price-sale" x="1072" y="664" text-anchor="middle">499</text>

    <text class="pitch" x="1037" y="733" text-anchor="middle">Let your clients book</text>
    <text class="pitch" x="1037" y="783" text-anchor="middle">their next appointment</text>
    <text class="pitch" x="1037" y="833" text-anchor="middle">using your app</text>

    <text class="platform" x="940" y="948" text-anchor="middle">Robodroid</text>
    <text class="platform" x="1140" y="948" text-anchor="middle">PommeOS</text>

    <g class="contact-web">
      <circle cx="933" cy="1028" r="10" fill="none" stroke="var(--magenta)" stroke-width="2"/>
      <ellipse cx="933" cy="1028" rx="4.5" ry="10" fill="none" stroke="var(--magenta)" stroke-width="1.6"/>
      <line x1="923" y1="1028" x2="943" y2="1028" stroke="var(--magenta)" stroke-width="1.6"/>
      <text class="contact" x="955" y="1035">www.website.com</text>
    </g>
    <g class="contact-mail">
      <rect x="922" y="1055" width="21" height="14" fill="none" stroke="var(--magenta)" stroke-width="2"/>
      <polyline points="922,1055 932.5,1064 943,1055" fill="none" stroke="var(--magenta)" stroke-width="2"/>
      <text class="contact" x="955" y="1069">info@website.com</text>
    </g>
  </g>
</svg>
</body>
</html>
```